Need business cards for our e-assessment business

We need professional looking business cards for our e-assessment business based in Europe. Our company is called Velnor.

You can just use sample name and addresses.

The colours we use are:

#70abe4 (blue)
#FF6600 (orange)

The back side should say: E-assessment made easy

This is the print-shop we are using. Please look at the link for info about formats: http://nl.printqet.com/help/faq/using-my-own-artwork.html

Target Market(s)

Target market is education and large corporations

Industry/Entity Type

Business

```html
<!DOCTYPE html>
<html lang="en">
<head>
<meta charset="utf-8">
<title>Velnor business cards</title>
<link rel="stylesheet" href="https://fonts.googleapis.com/css2?family=Montserrat:wght@400;500;600&display=swap">
<style>
  :root {
    --orange: #f26522;
    --brand-blue: #70abe4;
    --charcoal: #2c2c2e;
    --ink: #3a3a3c;
    --muted: #555558;
    --paper: #ffffff;
    --paper-shade: #ececec;
    --backdrop: #e6e4e1;
  }
  * { box-sizing: border-box; margin: 0; padding: 0; }
  html, body {
    width: 1200px;
    height: 871px;
    overflow: hidden;
    background: var(--backdrop);
    font-family: "Montserrat", sans-serif;
  }
  .stage {
    position: relative;
    width: 1200px;
    height: 871px;
  }
  .card {
    position: absolute;
    top: 268px;
    width: 520px;
    height: 336px;
    border-radius: 3px;
    box-shadow: 0 10px 28px rgba(0,0,0,0.22);
    overflow: hidden;
  }
  /* Back side */
  .card--back {
    left: 60px;
    background: var(--charcoal);
    display: flex;
    flex-direction: column;
    align-items: center;
    justify-content: center;
  }
  .back-name {
    color: var(--orange);
    font-size: 40px;
    font-weight: 500;
    letter-spacing: 6px;
    text-transform: uppercase;
  }
  .tagline {
    margin-top: 22px;
    color: var(--brand-blue);
    font-size: 15px;
    font-weight: 500;
    letter-spacing: 2px;
  }
  /* Front side */
  .card--front {
    left: 620px;
    background: linear-gradient(120deg, var(--paper) 45%, var(--paper-shade) 100%);
  }
  .brand-name {
    position: absolute;
    left: 32px;
    top: 196px;
    color: var(--orange);
    font-size: 30px;
    font-weight: 500;
    letter-spacing: 5px;
    text-transform: uppercase;
    line-height: 1;
  }
  .contact {
    position: absolute;
    left: 292px;
    top: 196px;
    color: var(--muted);
  }
  .contact-name {
    color: var(--ink);
    font-size: 16px;
    font-weight: 500;
    letter-spacing: 1.5px;
  }
  .contact-company {
    margin-top: 8px;
    color: var(--orange);
    font-size: 11px;
    font-weight: 600;
  }
  .contact-address {
    margin-top: 8px;
    font-size: 11px;
    font-weight: 500;
    line-height: 1.6;
    letter-spacing: 0.3px;
  }
</style>
</head>
<body>
  <main class="stage">
    <section class="card card--back" aria-label="Card back">
      <p class="back-name">Velnor</p>
      <p class="tagline">E-assessment made easy</p>
    </section>

    <section class="card card--front" aria-label="Card front">
      <p class="brand-name">Velnor</p>
      <div class="contact">
        <p class="contact-name">Maren K Doyle</p>
        <p class="contact-company">velnor inc</p>
        <p class="contact-address">14 Harbor Lane, Eastvale<br>QLD 4210</p>
      </div>
    </section>
  </main>
</body>
</html>
```